Book cover needed for self help business book

Book cover needed and I will provide back cover blurb and barcode to the winning designer. Book may be too small for spine, but I will give you the page number details to confirm. Book information below:

Title: Nine Winters a Trader
Subtitle: Proven Market Methods That Keep Paying Off Now
Author: Maribel Okonte

Design should be clean, modern, and bold—something that appeals to everyday entrepreneurs and resellers. The cover should reflect grit, real-world hustle, and long-term wisdom without looking overly corporate or flashy. I am open to your creative ideas.

I am open to modern designs, but also designs of rugged old covers that simulate a book that may have aged over the years.

I prefer not to have pictures or silhouettes of people

Requirements
Nice to have
• I am open to modern designs, but also designs of rugged old covers that simulate a book that may have aged over the years.
Should not have
• Pictures or silhouettes of people

```html
<!DOCTYPE html>
<html lang="en">
<head>
<meta charset="utf-8">
<title>Nine Winters a Trader — Book Cover</title>
<link href="https://fonts.googleapis.com/css2?family=Oswald:wght@400;500;700&display=swap" rel="stylesheet">
<style>
  :root {
    --page: #ffffff;
    --cover-core: #9b3424;
    --cover-mid: #74241a;
    --cover-edge: #2a0906;
    --accent: #f15a2f;
    --extrude: #2a0503;
    --headline: #ffffff;
    --note: #f4e479;
    --note-ink: #2a120c;
  }
  html, body {
    margin: 0;
    padding: 0;
    width: 1200px;
    height: 1200px;
    overflow: hidden;
    background: var(--page);
  }
  .canvas {
    display: block;
    width: 1200px;
    height: 1200px;
  }
  .numeral-word {
    font-family: "Oswald", sans-serif;
    font-weight: 700;
    font-size: 400px;
  }
  .title-line {
    font-family: "Oswald", sans-serif;
    font-weight: 700;
    font-size: 128px;
    fill: var(--headline);
  }
  .note-text {
    font-family: "Oswald", sans-serif;
    font-weight: 500;
    font-size: 19px;
    fill: var(--note-ink);
  }
  .byline {
    font-family: "Oswald", sans-serif;
    font-size: 17px;
    letter-spacing: 3px;
    fill: var(--accent);
  }
  .byline .byline-label { font-weight: 400; }
  .byline .byline-name { font-weight: 500; }
</style>
</head>
<body>
<svg class="canvas" viewBox="0 0 1200 1200" xmlns="http://www.w3.org/2000/svg" aria-label="Book cover: Nine Winters a Trader by Maribel Okonte">
  <defs>
    <radialGradient id="coverTone" cx="0.5" cy="0.5" r="0.72">
      <stop offset="0" stop-color="var(--cover-core)"/>
      <stop offset="0.65" stop-color="var(--cover-mid)"/>
      <stop offset="1" stop-color="var(--cover-edge)"/>
    </radialGradient>
  </defs>

  <!-- cover board: texture area -->
  <rect class="cover-texture" x="257" y="156" width="686" height="887" fill="url(#coverTone)" role="img" aria-label="Rugged, aged dark red grunge texture with darkened edges"/>

  <!-- big orange word with extruded shadow -->
  <g class="numeral-block">
    <g fill="var(--extrude)">
      <text class="numeral-word" x="370" y="598" textLength="462" lengthAdjust="spacingAndGlyphs">NINE</text>
      <text class="numeral-word" x="373" y="601" textLength="462" lengthAdjust="spacingAndGlyphs">NINE</text>
      <text class="numeral-word" x="376" y="604" textLength="462" lengthAdjust="spacingAndGlyphs">NINE</text>
      <text class="numeral-word" x="379" y="607" textLength="462" lengthAdjust="spacingAndGlyphs">NINE</text>
      <text class="numeral-word" x="382" y="610" textLength="462" lengthAdjust="spacingAndGlyphs">NINE</text>
      <text class="numeral-word" x="385" y="613" textLength="462" lengthAdjust="spacingAndGlyphs">NINE</text>
      <text class="numeral-word" x="388" y="616" textLength="462" lengthAdjust="spacingAndGlyphs">NINE</text>
    </g>
    <text class="numeral-word" x="366" y="594" textLength="462" lengthAdjust="spacingAndGlyphs" fill="var(--accent)">NINE</text>
  </g>

  <!-- subtitle area: pinned note -->
  <rect class="subtitle-note" x="729" y="324" width="179" height="191" fill="var(--note)" role="img" aria-label="Yellow sticky note pinned to the cover"/>
  <text class="note-text" text-anchor="middle">
    <tspan x="818" y="378">PROVEN</tspan>
    <tspan x="818" y="401">MARKET METHODS</tspan>
    <tspan x="818" y="424">THAT KEEP</tspan>
    <tspan x="818" y="447">PAYING OFF</tspan>
    <tspan x="818" y="470">NOW</tspan>
  </text>

  <!-- remaining title -->
  <text class="title-line" x="366" y="774" textLength="474" lengthAdjust="spacingAndGlyphs">WINTERS A</text>
  <text class="title-line" x="363" y="916" textLength="478" lengthAdjust="spacingAndGlyphs">TRADER</text>

  <!-- byline -->
  <line class="byline-rule" x1="361" y1="991" x2="838" y2="991" stroke="var(--accent)" stroke-width="1.2"/>
  <text class="byline" x="600" y="1024" text-anchor="middle"><tspan class="byline-label">AUTHOR - </tspan><tspan class="byline-name">MARIBEL OKONTE</tspan></text>
</svg>
</body>
</html>
```